Business Card Design Project

beauty / make up / lashes

Industry/Entity Type

Business

Contact Information for Business Card

pink / gold / wait / black vintage classic elegant design

```html
<!DOCTYPE html>
<html lang="en">
<head>
<meta charset="utf-8">
<title>Aure Lashes – Business Card</title>
<link href="https://fonts.googleapis.com/css2?family=Source+Sans+3:wght@300;400;600&display=swap" rel="stylesheet">
<style>
  :root {
    --stage: #e9e6e2;
    --card: #0d0d0d;
    --gold: #e3bd12;
    --ink: #f2f2f2;
    --silver: #c9c9c9;
    --shadow: rgba(0, 0, 0, 0.28);
  }
  * { box-sizing: border-box; margin: 0; padding: 0; }
  html, body {
    width: 1200px;
    height: 900px;
    overflow: hidden;
    background: var(--stage);
    font-family: "Source Sans 3", "Myriad Pro", sans-serif;
  }
  .stage {
    position: relative;
    width: 1200px;
    height: 900px;
    display: flex;
    align-items: center;
    justify-content: center;
    gap: 60px;
  }
  .card {
    position: relative;
    width: 525px;
    height: 300px;
    background: var(--card);
    box-shadow: 0 14px 30px var(--shadow);
  }

  /* Contact side */
  .card--contact {
    display: flex;
    align-items: center;
  }
  .brand-block {
    width: 262px;
    display: flex;
    align-items: center;
    justify-content: center;
    gap: 12px;
  }
  .brand-dot {
    width: 16px;
    height: 16px;
    border-radius: 50%;
    background: var(--gold);
  }
  .brand-name--gold {
    color: var(--gold);
    font-weight: 600;
    font-size: 30px;
    letter-spacing: 0.5px;
  }
  .divider {
    width: 1px;
    height: 176px;
    background: var(--gold);
  }
  .details {
    padding-left: 26px;
    color: var(--ink);
    font-size: 14px;
    line-height: 1.25;
  }
  .person-name {
    color: var(--gold);
    font-weight: 600;
    font-size: 17px;
  }
  .person-role { margin-bottom: 16px; }
  .address { margin-bottom: 14px; }
  .contact-list { list-style: none; }
  .contact-list li {
    display: flex;
    align-items: center;
    gap: 8px;
    margin-bottom: 1px;
  }
  .icon { width: 11px; height: 11px; flex: none; }
  .icon * { fill: var(--gold); }

  /* Brand side */
  .card--brand {
    display: flex;
    align-items: center;
    justify-content: center;
  }
  .brand-name--silver {
    color: var(--silver);
    font-weight: 300;
    font-size: 46px;
    letter-spacing: 2px;
  }
</style>
</head>
<body>
  <main class="stage">
    <section class="card card--contact" aria-label="Business card, contact side">
      <div class="brand-block">
        <span class="brand-dot"></span>
        <span class="brand-name--gold">Aure Lashes</span>
      </div>
      <div class="divider"></div>
      <div class="details">
        <p class="person-name">Elias Marlow</p>
        <p class="person-role">Managing Director</p>
        <p class="address">48 Linden Row, Suite 2<br>Westmoor, 560214.</p>
        <ul class="contact-list">
          <li>
            <svg class="icon" viewBox="0 0 12 12" aria-hidden="true"><path d="M2.5 0.8 4.4 2.9 3.4 4.3c.8 1.7 2.1 3 3.8 3.8l1.4-1 2.1 1.9-1 2.2C5 11 1 7 0.5 1.8z"/></svg>
            <span>044-555 201 348</span>
          </li>
          <li>
            <svg class="icon" viewBox="0 0 12 12" aria-hidden="true"><path d="M0.5 2.5h11v7h-11z"/><path d="M0.5 2.5 6 7l5.5-4.5" style="fill:none;stroke:#0d0d0d;stroke-width:1"/></svg>
            <span>hello@aurelashes.com</span>
          </li>
          <li>
            <svg class="icon" viewBox="0 0 12 12" aria-hidden="true"><circle cx="6" cy="6" r="5.5"/><path d="M1 6h10M6 0.5c2.2 2.6 2.2 8.4 0 11M6 0.5c-2.2 2.6-2.2 8.4 0 11" style="fill:none;stroke:#0d0d0d;stroke-width:0.8"/></svg>
            <span>www.aurelashes.com</span>
          </li>
        </ul>
      </div>
    </section>

    <section class="card card--brand" aria-label="Business card, brand side">
      <span class="brand-name--silver">Aure Lashes</span>
    </section>
  </main>
</body>
</html>
```